New Modern floristry business design

Hi, we are a new business based in Sydney called "velvet moss floristry"

With so many floristry's we need a good design that will set a great first impression.

A few descriptive words on how we envision velvet moss floristry:

-dynamic design
-minimal colour (colour can be used to enhance the design)
-black white grey (can include gold,silver,metallic shadowing)
Strong "VELVET MOSS" with a classy "FLORISTRY"
Bold with a touch of feminine

Industry/Entity Type

Business

Contact Information for Business Card

Velvet Moss Floristry,
Delphine Ruvek,
Velvetmossfloristry@quillmail.com.au

```html
<!DOCTYPE html>
<html lang="en">
<head>
<meta charset="utf-8">
<title>Velvet Moss Floristry — Business Card</title>
<link rel="stylesheet" href="https://fonts.googleapis.com/css2?family=Gelasio:wght@400&display=swap">
<style>
  :root {
    --backdrop: #d9d9d9;
    --card-black: #0b0b0b;
    --pattern-dark: #141414;
    --pattern-mid: #2c2c2c;
    --band-white: #fbfbfb;
    --silver: #d8d8d8;
    --ink-grey: #5a5a5a;
  }
  * { box-sizing: border-box; margin: 0; padding: 0; }
  html, body {
    width: 1200px;
    height: 900px;
    overflow: hidden;
    background: var(--backdrop);
  }
  .canvas {
    position: relative;
    width: 1200px;
    height: 900px;
    display: flex;
    align-items: center;
    justify-content: center;
  }
  .business-card {
    position: relative;
    width: 1000px;
    height: 570px;
    background: var(--card-black);
    overflow: hidden;
    font-family: "Gelasio", Georgia, serif;
  }
  .damask-field {
    position: absolute;
    left: 0;
    top: 0;
    width: 100%;
    height: 355px;
    background: radial-gradient(ellipse at 50% 40%, var(--pattern-mid) 0%, var(--pattern-dark) 60%, var(--card-black) 100%);
  }
  .brand {
    position: absolute;
    left: 0;
    top: 72px;
    width: 100%;
    display: flex;
    flex-direction: column;
    align-items: center;
    color: var(--silver);
    font-weight: 400;
  }
  .brand-mark {
    width: 22px;
    height: 22px;
    border-radius: 50%;
    background: var(--silver);
    margin-bottom: 34px;
  }
  .brand-name {
    display: flex;
    flex-direction: column;
    align-items: center;
    line-height: 1;
  }
  .brand-name-primary {
    font-size: 66px;
    letter-spacing: 4px;
  }
  .brand-name-secondary {
    margin-top: 16px;
    font-size: 34px;
    letter-spacing: 14px;
    padding-left: 14px;
  }
  .contact-band {
    position: absolute;
    left: 0;
    top: 355px;
    width: 100%;
    height: 115px;
    background: var(--band-white);
    display: flex;
    flex-direction: column;
    align-items: center;
    justify-content: center;
    gap: 4px;
    color: var(--ink-grey);
  }
  .contact-name { font-size: 29px; }
  .contact-email { font-size: 29px; }
</style>
</head>
<body>
  <main class="canvas">
    <article class="business-card">
      <div class="damask-field" role="img" aria-label="Dark grey floral damask pattern covering the upper card"></div>
      <header class="brand">
        <span class="brand-mark"></span>
        <h1 class="brand-name">
          <span class="brand-name-primary">VELVET MOSS</span>
          <span class="brand-name-secondary">floristry</span>
        </h1>
      </header>
      <section class="contact-band">
        <p class="contact-name">Delphine Ruvek</p>
        <p class="contact-email">Velvetmossfloristry@quillmail.com.au</p>
      </section>
    </article>
  </main>
</body>
</html>
```